Fairhollow Terrace
MAKE OUR HOME YOUR HOME
Professional
Delphine Marquist
Administrator
812 Quillon Avenue
Tea,SD 57064
delphine.marquist@fairhollowterrace.org
www.fairhollowterrace.org
Here is the AI file.

```html
<!DOCTYPE html>
<html lang="en">
<head>
<meta charset="utf-8">
<title>Fairhollow Terrace Stationery</title>
<link href="https://fonts.googleapis.com/css2?family=Cinzel:wght@600&family=Lato:wght@400;700&display=swap" rel="stylesheet">
<style>
  :root {
    --backdrop: #efefef;
    --paper: #ffffff;
    --brown: #5b3219;
    --brown-dark: #3b1d0b;
    --brown-light: #7a4a2a;
    --faint: #eee4dd;
    --ink: #4a4a4a;
    --cream: #f7efe8;
  }
  * { margin: 0; padding: 0; box-sizing: border-box; }
  html, body { width: 1200px; height: 857px; overflow: hidden; background: var(--backdrop); }
  .canvas { position: relative; width: 1200px; height: 857px; font-family: 'Lato', sans-serif; }
  .sheet { position: absolute; background: var(--paper); box-shadow: 0 1px 4px rgba(0,0,0,.18); overflow: hidden; }

  .brand { font-family: 'Cinzel', serif; font-weight: 600; color: var(--brown); line-height: 1.05; text-align: center; display: flex; align-items: center; gap: 6px; }
  .brand-mark { width: 10px; height: 10px; background: var(--brown); flex: none; }
  .brand-name { letter-spacing: .04em; white-space: nowrap; }
  .brand.on-dark { color: var(--cream); }
  .brand.on-dark .brand-mark { background: var(--cream); }

  .watermark { position: absolute; font-family: 'Cinzel', serif; font-weight: 600; color: var(--faint); text-align: center; line-height: 1; letter-spacing: .04em; }

  .band { position: absolute; left: 0; width: 100%; }
  .band-text { position: absolute; left: 0; width: 100%; text-align: center; color: var(--cream); font-size: 7px; line-height: 1.5; letter-spacing: .02em; white-space: nowrap; }
  .band-text span { color: var(--cream); }

  /* letterhead */
  .letterhead { left: 40px; top: 48px; width: 493px; height: 752px; }
  .letterhead .brand { position: absolute; left: 24px; top: 24px; font-size: 15px; }
  .letterhead .watermark { left: 0; width: 100%; top: 500px; font-size: 44px; }
  .letterhead .band { bottom: 0; height: 96px; }
  .letterhead .band-text { bottom: 8px; }

  /* business cards */
  .card-front { left: 576px; top: 43px; width: 221px; height: 130px; }
  .card-front .brand { position: absolute; left: 0; width: 100%; justify-content: center; top: 16px; font-size: 10px; }
  .card-person { position: absolute; left: 0; width: 100%; top: 58px; text-align: center; color: var(--ink); }
  .card-person .person-name { font-size: 8.5px; }
  .card-person .person-role { font-size: 6px; margin-top: 2px; }
  .card-front .band { bottom: 0; height: 34px; }
  .card-front .band-text { bottom: 4px; font-size: 5px; }

  .card-back { left: 811px; top: 43px; width: 221px; height: 130px; background: linear-gradient(180deg, var(--brown-light), var(--brown-dark)); }
  .card-back .brand { position: absolute; left: 0; width: 100%; justify-content: center; top: 54px; font-size: 11px; }

  /* long envelope */
  .envelope { left: 576px; top: 197px; width: 562px; height: 273px; }
  .envelope .brand { position: absolute; left: 28px; top: 30px; font-size: 13px; }
  .envelope .watermark { left: 0; width: 100%; top: 142px; font-size: 34px; }
  .envelope .band { bottom: 0; height: 70px; }
  .envelope .band-text { bottom: 7px; font-size: 6.5px; }

  /* envelope back */
  .envelope-back { left: 576px; top: 504px; width: 562px; height: 259px; }
  .envelope-back .flap { position: absolute; left: 0; top: 0; width: 100%; height: 92px; }
  .envelope-back .brand { position: absolute; left: 0; width: 100%; justify-content: center; top: 30px; font-size: 13px; }
</style>
</head>
<body>
<main class="canvas">

  <section class="sheet letterhead" aria-label="Letterhead">
    <div class="brand"><span class="brand-mark"></span><span class="brand-name">Fairhollow<br>Terrace</span></div>
    <div class="watermark">FAIRHOLLOW<br>TERRACE</div>
    <svg class="band" viewBox="0 0 493 96" preserveAspectRatio="none">
      <defs><linearGradient id="bandLH" x1="0" y1="0" x2="0" y2="1"><stop offset="0" stop-color="#7a4a2a"/><stop offset="1" stop-color="#3b1d0b"/></linearGradient></defs>
      <path d="M0 70 Q246 30 493 70 L493 96 L0 96 Z" fill="url(#bandLH)"/>
    </svg>
    <div class="band-text">812 Quillon Avenue, Larkmoor, SD 57912 &nbsp;|&nbsp; Phone: (605) 555-0148<br>Email: <span>delphine.marquist@fairhollowterrace.org</span> &nbsp;|&nbsp; <span>www.fairhollowterrace.org</span></div>
  </section>

  <section class="sheet card-front" aria-label="Business card front">
    <div class="brand"><span class="brand-mark"></span><span class="brand-name">Fairhollow<br>Terrace</span></div>
    <div class="card-person">
      <div class="person-name">Delphine Marquist</div>
      <div class="person-role">Administrator</div>
    </div>
    <svg class="band" viewBox="0 0 221 34" preserveAspectRatio="none">
      <defs><linearGradient id="bandBC" x1="0" y1="0" x2="0" y2="1"><stop offset="0" stop-color="#7a4a2a"/><stop offset="1" stop-color="#3b1d0b"/></linearGradient></defs>
      <path d="M0 18 Q110 6 221 18 L221 34 L0 34 Z" fill="url(#bandBC)"/>
    </svg>
    <div class="band-text">812 Quillon Avenue, Larkmoor, SD 57912 | Phone: (605) 555-0148<br><span>delphine.marquist@fairhollowterrace.org</span> | <span>www.fairhollowterrace.org</span></div>
  </section>

  <section class="sheet card-back" aria-label="Business card back">
    <div class="brand on-dark"><span class="brand-mark"></span><span class="brand-name">Fairhollow<br>Terrace</span></div>
  </section>

  <section class="sheet envelope" aria-label="Envelope front">
    <div class="brand"><span class="brand-mark"></span><span class="brand-name">Fairhollow<br>Terrace</span></div>
    <div class="watermark">FAIRHOLLOW<br>TERRACE</div>
    <svg class="band" viewBox="0 0 562 70" preserveAspectRatio="none">
      <defs><linearGradient id="bandEN" x1="0" y1="0" x2="0" y2="1"><stop offset="0" stop-color="#7a4a2a"/><stop offset="1" stop-color="#3b1d0b"/></linearGradient></defs>
      <path d="M0 44 Q281 18 562 44 L562 70 L0 70 Z" fill="url(#bandEN)"/>
    </svg>
    <div class="band-text">812 Quillon Avenue, Larkmoor, SD 57912 &nbsp;|&nbsp; Phone: (605) 555-0148<br>Email: <span>delphine.marquist@fairhollowterrace.org</span> &nbsp;|&nbsp; <span>www.fairhollowterrace.org</span></div>
  </section>

  <section class="sheet envelope-back" aria-label="Envelope back">
    <svg class="flap" viewBox="0 0 562 92" preserveAspectRatio="none">
      <defs><linearGradient id="flapGrad" x1="0" y1="0" x2="0" y2="1"><stop offset="0" stop-color="#3b1d0b"/><stop offset="1" stop-color="#7a4a2a"/></linearGradient></defs>
      <path d="M0 0 L562 0 L562 70 Q281 100 0 70 Z" fill="url(#flapGrad)"/>
    </svg>
    <div class="brand on-dark"><span class="brand-mark"></span><span class="brand-name">Fairhollow<br>Terrace</span></div>
  </section>

</main>
</body>
</html>
```